Bref créative
Bellquist law p.a.
See logo attached
Simple
Hal Bellquist
Board Certified Trial Lawyer
Post Office Box 48716
27 West Caldera Street
Pensacola, Florida. 30874
Hal@bellquistlegal.example
Www.halbellquist.example
Here is a version with a slight varation in the size of bellquist law
Here is the final version of the logo with the bellquist law text included with the font that I though was most suitable. There is a white outline on this version that is not on the final version. It is a tif file that will not upload to this server but is on my facebook page. I can email it privately if someone needs it. I think this logo may look better on grey paper. The black background that I have in this attachment may not be feasible since it would require three colors on the letterhead. Anyway, thanks for your help.

```html
<!DOCTYPE html>
<html lang="en">
<head>
<meta charset="utf-8">
<title>Bellquist Law P.A. — Stationery</title>
<link rel="stylesheet" href="https://fonts.googleapis.com/css2?family=Questrial&display=swap">
<style>
  :root{
    --paper:#ffffff;
    --canvas:#ffffff;
    --edge:#c9c9c9;
    --accent:#e8782a;
    --accent-faint:#fbe9dc;
    --ink:#555555;
    --ink-soft:#8a8a8a;
  }
  *{box-sizing:border-box;margin:0;padding:0}
  html,body{width:1200px;height:1101px;overflow:hidden;background:var(--canvas)}
  body{position:relative;font-family:"Questrial",Arial,sans-serif;color:var(--ink)}

  .letterhead{position:absolute;left:45px;top:15px;width:720px;height:1050px;background:var(--paper);border:1px solid var(--edge);box-shadow:2px 3px 6px rgba(0,0,0,.12)}
  .brand{position:absolute;left:0;right:0;text-align:center;color:var(--accent);white-space:nowrap}
  .brand .dot{display:inline-block;border-radius:50%;background:var(--accent);vertical-align:middle}
  .letterhead .brand{top:70px;font-size:30px;letter-spacing:1px}
  .letterhead .brand .dot{width:14px;height:14px;margin-right:10px}
  .letterhead .watermark{position:absolute;left:40px;top:400px;font-size:64px;color:var(--accent-faint);letter-spacing:2px;white-space:nowrap}
  .letterhead .footer-rule{position:absolute;left:40px;right:40px;top:985px;border-top:1.5px solid var(--accent)}
  .letterhead .footer{position:absolute;left:40px;right:40px;top:1000px;text-align:center;color:var(--accent);font-size:13px;line-height:20px}

  .card{position:absolute;left:855px;top:120px;width:315px;height:180px;background:var(--paper);border:1px solid var(--edge);box-shadow:2px 3px 6px rgba(0,0,0,.12)}
  .card .brand{left:0;right:auto;width:150px;top:22px;font-size:12px;text-align:center}
  .card .brand .dot{width:7px;height:7px;margin-right:5px}
  .card .person{position:absolute;left:160px;top:70px}
  .card .name{color:var(--accent);font-size:15px}
  .card .title{font-size:9px;color:var(--ink-soft);margin-top:3px}
  .card .contact{position:absolute;left:20px;right:20px;top:122px;font-size:8.5px;line-height:13px;color:var(--ink)}

  .envelope{position:absolute;left:420px;top:390px;width:750px;height:600px}
  .envelope svg{position:absolute;inset:0}
  .envelope .brand.flap{top:60px;font-size:12px}
  .envelope .brand.flap .dot{width:7px;height:7px;margin-right:5px}
  .envelope .brand.main{top:300px;font-size:26px;letter-spacing:1px}
  .envelope .brand.main .dot{width:12px;height:12px;margin-right:8px}
  .envelope .return{position:absolute;left:0;right:0;top:540px;text-align:center;font-size:11px;color:var(--ink)}
</style>
</head>
<body>

<section class="letterhead" aria-label="Letterhead">
  <div class="brand"><span class="dot"></span>Bellquist law p.a.</div>
  <div class="watermark" aria-hidden="true">Bellquist law p.a.</div>
  <div class="footer-rule"></div>
  <p class="footer">Post Office Box 48716 &nbsp;27 West Caldera Street Pensacola, Florida, 30874 &nbsp;P: 850 555 0142<br>
  F: 850 555 0187 &nbsp;Hal@bellquistlegal.example &nbsp;Www.halbellquist.example</p>
</section>

<section class="envelope" aria-label="Envelope">
  <svg width="750" height="600" viewBox="0 0 750 600">
    <rect x="0.5" y="0.5" width="749" height="599" fill="#ffffff" stroke="#c9c9c9"/>
    <polyline points="1,1 375,180 749,1" fill="none" stroke="#c9c9c9" stroke-width="1"/>
    <line x1="40" y1="525" x2="710" y2="525" stroke="#e8782a" stroke-width="1.2"/>
  </svg>
  <div class="brand flap"><span class="dot"></span>Bellquist law p.a.</div>
  <div class="brand main"><span class="dot"></span>Bellquist law p.a.</div>
  <p class="return">Post Office Box 48716 &nbsp;27 West Caldera Street Pensacola, Florida, 30874</p>
</section>

<section class="card" aria-label="Business card">
  <div class="brand"><span class="dot"></span>Bellquist law p.a.</div>
  <div class="person">
    <p class="name">Hal Bellquist</p>
    <p class="title">Board Certified Trial Lawyer</p>
  </div>
  <p class="contact">Post Office Box 48716 &nbsp;27 West Caldera Street Pensacola, Florida, 30874<br>
  P: 850 555 0142 &nbsp;F: 850 555 0187 &nbsp;Hal@bellquistlegal.example &nbsp;Www.halbellquist.example</p>
</section>

</body>
</html>
```